Marco Velin Landing page

I need a Landing page for a website Marco Velin. This is for an upscale clothing store for Men and Womens clothing and other items. It has to be elegant and unique in design and style.

Target Market(s)

Men, Women, Young adults 18-60

Coding

Coded - Design and coding required

Number of Pages Required

1 page

Font styles to use
Decorative

Colors

Designer to choose colors to be used in the design.

```html
<!DOCTYPE html>
<html lang="en">
<head>
<meta charset="utf-8">
<title>Marco Velin — Landing</title>
<link rel="stylesheet" href="https://fonts.googleapis.com/css2?family=Roboto:wght@400;500;700&display=swap">
<style>
  :root {
    --ink: #1d1a1b;
    --ink-soft: #231f20;
    --gold: #d9b25e;
    --gold-light: #f3d58c;
    --gold-deep: #c99a45;
  }
  * { margin: 0; padding: 0; box-sizing: border-box; }
  html, body { width: 1200px; height: 775px; overflow: hidden; background: var(--ink); }
  .page { position: relative; width: 1200px; height: 775px; overflow: hidden; font-family: 'Roboto', sans-serif; }

  .hero-visual {
    position: absolute; inset: 0;
    background:
      radial-gradient(ellipse 260px 420px at 600px 520px, rgba(190,150,100,0.55), transparent 70%),
      radial-gradient(ellipse 600px 260px at 600px 110px, #f4efe6, transparent 80%),
      linear-gradient(90deg, #b8a49a 0%, #cdbdb0 22%, #e9dccb 50%, #e8d2b8 78%, #d8b99a 100%);
  }
  .hero-visual::after {
    content: ""; position: absolute; inset: 0;
    background: linear-gradient(180deg, rgba(255,255,255,0.25) 0%, rgba(0,0,0,0) 40%, rgba(120,90,70,0.18) 100%);
  }

  .topbar {
    position: absolute; left: 0; top: 0; width: 1200px; height: 97px;
    background: var(--ink-soft);
  }
  .brand {
    position: absolute; left: 0; top: 0; width: 240px; height: 185px;
    background: var(--ink);
    display: flex; align-items: center; justify-content: center;
    text-decoration: none;
    box-shadow: 2px 2px 6px rgba(0,0,0,0.3);
  }
  .brand-name {
    font-family: 'Roboto', sans-serif; font-weight: 500; font-size: 24px;
    color: var(--gold); letter-spacing: 2px; white-space: nowrap; text-transform: uppercase;
  }

  .main-nav a {
    position: absolute; top: 37px;
    font-size: 17.6px; font-weight: 500; color: var(--gold-light);
    text-decoration: none; letter-spacing: 0.2px; line-height: 22px;
  }
  .main-nav .is-active::after {
    content: ""; position: absolute; left: -4px; top: 41px; width: 52px; height: 3px;
    background: linear-gradient(90deg, var(--gold-deep), var(--gold), rgba(217,178,94,0));
  }

  .lang-tab {
    position: absolute; left: 1021px; top: 0; width: 57px; height: 133px;
    background: linear-gradient(180deg, #e8c777 0%, var(--gold) 100%);
    border-radius: 0 0 29px 29px;
    color: var(--ink); font-size: 17.6px; font-weight: 500; text-align: center; padding-top: 38px;
  }
  .lang-tab svg { display: block; margin: 6px auto 0; }

  .icon-btn { position: absolute; top: 35px; }
  .divider { position: absolute; left: 1136px; top: 0; width: 1px; height: 97px; background: #3a3536; }

  .slide-arrow { position: absolute; top: 454px; }

  .promo {
    position: absolute; left: 0; top: 420px; width: 1200px; text-align: center;
  }
  .promo-title {
    font-size: 48px; font-weight: 700; color: var(--ink); letter-spacing: -0.5px; line-height: 1;
    margin-top: 6px;
  }
  .promo-offer {
    display: block; margin: 10px auto 0; width: 474px; height: 50px;
    background: linear-gradient(90deg, #f3d58c 0%, #f5dd9c 50%, #f3d58c 100%);
    font-size: 30px; font-weight: 500; color: var(--ink); letter-spacing: 14.5px;
    line-height: 50px; padding-left: 14px;
  }
  .promo-note {
    margin-top: 12px; font-size: 14px; line-height: 16px; color: var(--ink-soft); letter-spacing: 0.2px;
  }
  .cta {
    position: absolute; left: 488px; top: 586px; width: 219px; height: 44px;
    background: linear-gradient(90deg, rgba(29,26,27,0) 0%, rgba(29,26,27,0.85) 25%, var(--ink) 50%);
    color: var(--gold); font-size: 22px; font-weight: 700; letter-spacing: 1.5px;
    text-decoration: none; line-height: 44px;
  }
  .cta::before {
    content: ""; position: absolute; left: 17px; top: 22px; width: 46px; height: 2px; background: var(--gold);
  }
  .cta span { position: absolute; left: 74px; }
</style>
</head>
<body>
<div class="page">
  <div class="hero-visual" role="img" aria-label="Photo of a bearded man in glasses wearing a camel coat and black turtleneck in front of a softly blurred historic building"></div>

  <header class="topbar">
    <nav class="main-nav">
      <a href="#" class="is-active" style="left:284px">NEW</a>
      <a href="#" style="left:381px">CLOTHES</a>
      <a href="#" style="left:512px">SHOES</a>
      <a href="#" style="left:619px">ACCESSORIES</a>
      <a href="#" style="left:786px">SALE</a>
      <a href="#" style="left:878px">THE BRAND</a>
    </nav>
    <div class="lang-tab">EN
      <svg width="14" height="9" viewBox="0 0 14 9"><path d="M1.5 1.5 7 7l5.5-5.5" fill="none" stroke="#1d1a1b" stroke-width="2.6" stroke-linecap="round" stroke-linejoin="round"/></svg>
    </div>
    <svg class="icon-btn" style="left:1097px" width="24" height="24" viewBox="0 0 24 24" aria-label="Search">
      <circle cx="10" cy="10" r="7.5" fill="none" stroke="#d9b25e" stroke-width="2.6"/>
      <path d="M15.5 15.5 22 22" stroke="#d9b25e" stroke-width="3" stroke-linecap="round"/>
    </svg>
    <div class="divider"></div>
    <svg class="icon-btn" style="left:1153px;top:37px" width="30" height="22" viewBox="0 0 30 22" aria-label="Cart">
      <path d="M1 3h5l3 11h15" fill="none" stroke="#d9b25e" stroke-width="2.4" stroke-linecap="round" stroke-linejoin="round"/>
      <path d="M8 6h20M9 9h15M10 12h12" stroke="#d9b25e" stroke-width="2.2" stroke-linecap="round"/>
      <path d="M22 1 28 6" stroke="#d9b25e" stroke-width="2.2" stroke-linecap="round"/>
      <circle cx="11" cy="19" r="1.8" fill="#d9b25e"/><circle cx="21" cy="19" r="1.8" fill="#d9b25e"/>
    </svg>
  </header>

  <a class="brand" href="#"><span class="brand-name">Marco Velin</span></a>

  <svg class="slide-arrow" style="left:36px" width="58" height="96" viewBox="0 0 58 96" aria-label="Previous slide">
    <path d="M52 4 8 48l44 44" fill="none" stroke="rgba(255,255,255,0.55)" stroke-width="8"/>
  </svg>
  <svg class="slide-arrow" style="left:1106px" width="58" height="96" viewBox="0 0 58 96" aria-label="Next slide">
    <path d="M6 4l44 44L6 92" fill="none" stroke="rgba(255,255,255,0.55)" stroke-width="8"/>
  </svg>

  <section class="promo">
    <h1 class="promo-title">END OF SEASON SALE</h1>
    <span class="promo-offer">UP TO 70% OFF!</span>
    <p class="promo-note">LIMITED TIME ONLY</p>
  </section>
  <a class="cta" href="#"><span>SHOP NOW</span></a>
</div>
</body>
</html>
```